business card with logo Velmora Nails & Spa 2816 SW Quillan Ave Portland OR 97384

Would like to have a business card with our logo.
like bottle of polish with our logo or letter V on it
want something that first glance would let you know that it is a nail salon.
like the hands with polish bottle dripping.
like black or White back ground

Velmora Nails & Spa
(The Velvet Retreat)
2816 SW Quillan Ave
Portland, OR 97384
Call or Text: 1-503-555-0148
www.VelmoraNailsnSpa.example
Open 7 days a week.
After 7:00 PM is by appointment only.
Closed only on Thanksgiving & Christmas.

Target Market(s)

20%Man and 80%Woman 13-70

Industry/Entity Type

Business

Contact Information for Business Card

Elegant with Logo-Business name- address-phone-open days. closed day.

Font styles to use
Decorative
Script

Colors
000000

Requirements
Must have
• Logo and place for Technician Name
• Velmora Nails & Spa
• (The Velvet Retreat)
• 2816 SW Quillan Ave
• Portland, OR 97384
• Call or Text: 1-503-555-0148
• Open 7 days a week
• Closed only on Thanksgiving & Christmas.
• We accepted all major credit cards but prefer cash. Thank you
Nice to have
• Nail polish bottle with our Logo or letter V
Should not have
• too colorful

```html
<!DOCTYPE html>
<html lang="en">
<head>
<meta charset="utf-8">
<title>Velmora Nails &amp; Spa – Business Card</title>
<link href="https://fonts.googleapis.com/css2?family=Open+Sans:wght@400;600;700&display=swap" rel="stylesheet">
<style>
  :root {
    --stage: #3a3a3a;
    --card-black: #0b0b0b;
    --card-black-soft: #1a1a1a;
    --accent-yellow: #f2d500;
    --ink-white: #ffffff;
    --ink-dark: #111111;
    --pay-ink: #3c3c3c;
    --panel-white: #ffffff;
  }
  * { margin: 0; padding: 0; box-sizing: border-box; }
  html, body {
    width: 1200px;
    height: 874px;
    overflow: hidden;
    background: var(--stage);
    font-family: "Open Sans", sans-serif;
  }
  .business-card {
    position: absolute;
    left: 703px;
    top: 54px;
    width: 438px;
    height: 766px;
    background: radial-gradient(ellipse at 40% 30%, var(--card-black-soft), var(--card-black) 70%);
    overflow: hidden;
  }
  .polish-brush-art {
    position: absolute;
    left: 19px;
    top: 25px;
    width: 88px;
    height: 228px;
  }
  .polish-bottle-art {
    position: absolute;
    left: 29px;
    top: 327px;
    width: 135px;
    height: 221px;
  }
  .brand {
    position: absolute;
    left: 118px;
    top: 136px;
    width: 300px;
    text-align: center;
    color: var(--ink-white);
  }
  .brand-name {
    font-size: 50px;
    font-weight: 600;
    line-height: 60px;
    color: var(--accent-yellow);
    letter-spacing: 0.5px;
  }
  .brand-subtitle {
    font-size: 23px;
    line-height: 27px;
  }
  .brand-tagline {
    font-size: 20px;
    line-height: 25px;
  }
  .technician {
    position: absolute;
    right: 29px;
    top: 330px;
    text-align: right;
    color: var(--accent-yellow);
  }
  .technician-name {
    font-size: 24px;
    line-height: 30px;
    letter-spacing: 0.3px;
  }
  .technician-role {
    font-size: 17px;
    line-height: 22px;
  }
  .technician-bar {
    position: absolute;
    left: 425px;
    top: 326px;
    width: 12px;
    height: 58px;
    background: var(--accent-yellow);
  }
  .contact {
    position: absolute;
    left: 172px;
    top: 424px;
    color: var(--ink-white);
    font-size: 18.5px;
    line-height: 26px;
  }
  .contact-web {
    margin-top: 10px;
    font-size: 17px;
  }
  .info-panel {
    position: absolute;
    left: 0;
    top: 558px;
    width: 438px;
    height: 193px;
    background: var(--panel-white);
    color: var(--ink-dark);
    text-align: center;
  }
  .hours {
    padding-top: 8px;
    font-size: 18.5px;
    line-height: 23px;
  }
  .payment-row {
    display: flex;
    justify-content: center;
    gap: 10px;
    margin-top: 14px;
  }
  .payment-name {
    font-size: 16px;
    font-weight: 700;
    color: var(--pay-ink);
    line-height: 38px;
    padding: 0 4px;
  }
  .payment-note {
    margin-top: 6px;
    font-size: 16px;
    line-height: 20px;
  }
</style>
</head>
<body>
  <div class="business-card">
    <svg class="polish-brush-art" role="img" aria-label="White nail polish brush and cap illustration" viewBox="0 0 88 228">
      <rect x="0" y="0" width="88" height="228" fill="#ffffff" rx="4"/>
    </svg>

    <div class="brand">
      <div class="brand-name">Velmora</div>
      <div class="brand-subtitle">Nails n Spa</div>
      <div class="brand-tagline">The Velvet Retreat</div>
    </div>

    <div class="technician">
      <div class="technician-name">MARISA LEE KENT</div>
      <div class="technician-role">nail tehnician</div>
    </div>
    <div class="technician-bar"></div>

    <svg class="polish-bottle-art" role="img" aria-label="White nail polish bottle illustration with the letter V on its label" viewBox="0 0 135 221">
      <rect x="0" y="0" width="135" height="221" fill="#ffffff" rx="10"/>
    </svg>

    <div class="contact">
      <div>2816 SW Quillan Ave</div>
      <div>Portland, OR 97384</div>
      <div>Call or Text: 1-503-555-0148</div>
      <div class="contact-web">www.VelmoraNailsnSpa.example</div>
    </div>

    <div class="info-panel">
      <div class="hours">
        <div>Open 7 days a week.</div>
        <div>After 7:00 PM is by appointment only.</div>
        <div>Closed only on Thanksgiving &amp; Christmas.</div>
      </div>
      <div class="payment-row">
        <span class="payment-name">Trellis</span>
        <span class="payment-name">Corvo</span>
        <span class="payment-name">Ambrin</span>
        <span class="payment-name">Lumena</span>
      </div>
      <div class="payment-note">
        <div>We accepted all major credit cards</div>
        <div>but prefer cash. Thank you</div>
      </div>
    </div>
  </div>
</body>
</html>
```